General Dental Office Business Card

I run a private general dental office in southern California, and would like a refresh/redesign of my business card. I focus on quality care rather than volume. The email address on the uploaded current card should be updated to: info@marbleshoredental.example. The current card's logo is a deboss, but I am open to other ideas. The logo can be refreshed, but it is something that's been with me since the beginning of the office, so I wouldn't want a drastic redesign.
Target Market(s)
Adults 18-99, whoever needs dental services
Industry/Entity Type
Healthcare/Dental
Contact Information for Business Card
Name, Address, Phone, email
Colors
Designer to choose colors to be used in the design.
Requirements
Must have
- Logo (Same as original one in the uploaded file), space on back for appointment time/date

```html
<!DOCTYPE html>
<html lang="en">
<head>
<meta charset="utf-8">
<title>Marble Shore Dental – Business Card</title>
<link rel="stylesheet" href="https://fonts.googleapis.com/css2?family=Quicksand:wght@400;500;700&display=swap">
<style>
  :root {
    --backdrop: #e4e4e6;
    --card-white: #f4f4f5;
    --brand-blue: #7fd4ea;
    --ink-grey: #6a6a6e;
    --text-light: #f2fbfe;
    --shadow: 0 10px 28px rgba(0,0,0,0.14);
  }
  * { box-sizing: border-box; margin: 0; padding: 0; }
  html, body {
    width: 1200px; height: 1029px; overflow: hidden;
    background: var(--backdrop);
    font-family: "Quicksand", sans-serif;
  }
  .sheet {
    width: 1200px; height: 1029px;
    display: flex; flex-direction: column; align-items: center; justify-content: center;
    gap: 70px;
  }
  .card {
    width: 620px; height: 354px;
    background: var(--card-white);
    box-shadow: var(--shadow);
    position: relative;
    overflow: hidden;
  }

  /* Brand lockup: plain circle + practice name */
  .brand {
    display: flex; flex-direction: column; align-items: center; gap: 14px;
  }
  .brand-dot {
    width: 112px; height: 112px; border-radius: 50%;
    background: var(--brand-blue);
  }
  .brand-name {
    color: var(--brand-blue);
    font-weight: 400;
    font-size: 27px;
    letter-spacing: 0.5px;
    white-space: nowrap;
  }

  /* Front */
  .card--front {
    display: flex; align-items: center; justify-content: center;
  }

  /* Back */
  .card--back { display: flex; }
  .back-brand {
    width: 42%;
    display: flex; align-items: center; justify-content: center;
  }
  .back-brand .brand-dot { width: 96px; height: 96px; }
  .back-brand .brand-name { font-size: 19px; }
  .back-info {
    width: 58%;
    background: var(--brand-blue);
    padding: 44px 26px 22px 34px;
    display: flex; flex-direction: column;
  }
  .doctor-name {
    color: var(--ink-grey);
    font-weight: 700;
    font-size: 27px;
    letter-spacing: 0.2px;
    white-space: nowrap;
  }
  .specialty {
    display: block;
    margin-top: 4px;
    margin-right: -26px;
    margin-left: -6px;
    background: var(--card-white);
    color: var(--brand-blue);
    font-weight: 400;
    font-size: 17px;
    padding: 1px 0 2px 6px;
  }

  /* Appointment write-in area */
  .appointment {
    margin-top: 16px;
    color: var(--text-light);
    font-size: 13px;
    font-weight: 500;
  }
  .appointment-title {
    font-size: 13px;
    font-weight: 700;
    letter-spacing: 0.6px;
    text-transform: uppercase;
    margin-bottom: 6px;
  }
  .appointment-fields { display: flex; gap: 18px; }
  .appointment-field {
    flex: 1;
    display: flex; align-items: flex-end; gap: 6px;
  }
  .write-line {
    flex: 1;
    height: 16px;
    border-bottom: 1px solid var(--text-light);
  }

  .contact {
    margin-top: auto;
    color: var(--text-light);
    font-size: 15px;
    font-weight: 500;
    line-height: 1.42;
    font-style: normal;
    white-space: nowrap;
  }
  .contact .label { display: inline-block; width: 48px; }
</style>
</head>
<body>
  <main class="sheet">
    <section class="card card--front" aria-label="Card front">
      <div class="brand">
        <div class="brand-dot"></div>
        <span class="brand-name">Marble Shore Dental</span>
      </div>
    </section>

    <section class="card card--back" aria-label="Card back">
      <div class="back-brand">
        <div class="brand">
          <div class="brand-dot"></div>
          <span class="brand-name">Marble Shore Dental</span>
        </div>
      </div>
      <div class="back-info">
        <h1 class="doctor-name">Daniel R. Osei DDS</h1>
        <span class="specialty">General Dentistry</span>

        <div class="appointment">
          <p class="appointment-title">Next Appointment</p>
          <div class="appointment-fields">
            <div class="appointment-field"><span>Date</span><span class="write-line"></span></div>
            <div class="appointment-field"><span>Time</span><span class="write-line"></span></div>
          </div>
        </div>

        <address class="contact">
          1820 Harbor Crest Lane<br>
          Coral Bay, CA 92700<br>
          949-555-0147<br>
          <span class="label">email:</span>info@marbleshoredental.example<br>
          <span class="label">web:</span>www.marbleshoredental.example
        </address>
      </div>
    </section>
  </main>
</body>
</html>
```